Sales sheet for printing and embroidery apparel items - Copper Fern Prints

I would like a one page flyer or sales sheet that I would use as a template to send different images of apparel we produce. I have attached examples of layouts I like.
- Ideally, it would have space for 3-5 items.
- I would like it one page only - not a folding flyer.
- Our companies name is Copper Fern Prints.
- This will be used for many different products and markets so I don't need wording/copy. You can use wording from the 7Q7 or K81 flyer.

Colors
0054AA
0677BA
7BADD7
CADEEF
E8F1F8
00AB8E
00BBA5
67D7C9
C6EFE9
E9F9F6
FFC000
F8CF3A
FAE287
FDF2CF
FEFAEE

Requirements
Must have
• Places for between 3 and 5 images of apparel (t-shirts, hats etc)

```html
<!DOCTYPE html>
<html lang="en">
<head>
<meta charset="utf-8">
<title>Sample Merch Kit – Copper Fern Prints</title>
<link rel="stylesheet" href="https://fonts.googleapis.com/css2?family=Inter:wght@700;800&family=Montserrat:wght@400;500;600;700;800&family=Kaushan+Script&display=swap">
<style>
  :root {
    --page-bg: #c9cacc;
    --paper: #ffffff;
    --ink: #111111;
    --blue-deep: #0054AA;
    --blue: #0677BA;
    --blue-soft: #7BADD7;
    --blue-pale: #CADEEF;
    --blue-mist: #E8F1F8;
    --teal-deep: #00AB8E;
    --teal: #00BBA5;
    --teal-soft: #67D7C9;
    --gold: #FFC000;
    --gold-soft: #F8CF3A;
    --gold-pale: #FAE287;
    --charcoal: #1e2328;
  }
  * { box-sizing: border-box; margin: 0; padding: 0; }
  html, body { width: 1200px; height: 960px; overflow: hidden; background: var(--page-bg); }
  .sheet {
    position: absolute; left: 253px; top: 30px;
    width: 732px; height: 948px;
    transform: scale(0.949); transform-origin: top left;
    background: var(--paper);
    font-family: "Montserrat", sans-serif; color: var(--ink);
    overflow: hidden;
  }
  .abs { position: absolute; }
  .accent-bar { left: 0; top: 37px; width: 26px; height: 87px; background: linear-gradient(180deg, var(--gold), var(--teal-deep)); }
  .title { left: 48px; top: 30px; font-family: "Inter", sans-serif; font-weight: 800; font-size: 60px; letter-spacing: -1.5px; line-height: 72px; }
  .tagline { left: 51px; top: 101px; font-size: 21px; font-weight: 500; color: var(--blue-deep); letter-spacing: -0.3px; }
  .brand-mark { left: 585px; top: 48px; width: 110px; display: flex; flex-direction: column; align-items: center; gap: 6px; }
  .brand-mark .square { width: 50px; height: 50px; background: var(--teal-deep); }
  .brand-mark .name { font-weight: 800; font-size: 16px; line-height: 1.1; color: var(--blue-deep); text-align: center; }
  .series { left: 50px; top: 170px; font-size: 25px; font-weight: 600; line-height: 30px; }
  .kit-label { left: 48px; top: 287px; padding: 1px 4px; background: var(--blue); color: #fff; font-size: 15px; font-weight: 600; }
  .kit-list { left: 53px; top: 315px; font-size: 15px; line-height: 21px; list-style: none; }
  .kit-list li span { display: inline-block; width: 22px; }
  .colors { left: 53px; top: 398px; display: flex; align-items: center; gap: 4px; font-size: 15px; }
  .colors .label { margin-right: 8px; }
  .dot { width: 19px; height: 19px; border-radius: 50%; }
  .sizes { left: 53px; top: 421px; font-size: 15px; }
  .warning { left: 53px; top: 463px; width: 210px; font-size: 11px; line-height: 13.5px; }
  .side-tab { left: 342px; top: 171px; width: 40px; height: 216px; background: var(--blue-deep); border-bottom-left-radius: 24px; }
  .side-tab span, .model-label {
    position: absolute; white-space: nowrap; transform: rotate(-90deg); transform-origin: left top;
  }
  .side-tab span { left: 8px; top: 190px; color: #fff; font-size: 24px; letter-spacing: 0.5px; }
  .model-label { left: 353px; top: 463px; font-size: 16px; letter-spacing: 1px; }
  .photo { background: var(--blue-mist); }
  .hero { left: 380px; top: 171px; width: 303px; height: 347px; }
  .fill { position: absolute; inset: 30px 22px; border-radius: 40px 40px 14px 14px; }
  .thumb { top: 535px; width: 200px; height: 228px; z-index: 2; }
  .thumb .fill { inset: 26px 18px; }
  .t1 { left: 51px; } .t2 { left: 267px; } .t3 { left: 481px; }
  .footer { left: 0; top: 730px; width: 732px; height: 218px; background: var(--blue-deep); z-index: 1; }
  .footer-name { left: 50px; top: 800px; z-index: 2; color: var(--gold); font-weight: 800; font-size: 38px; line-height: 42px; letter-spacing: 0.5px; text-transform: uppercase; }
  .invite { right: 40px; top: 792px; z-index: 2; font-family: "Kaushan Script", cursive; color: var(--gold); font-size: 25px; line-height: 32px; }
  .contact { right: 44px; top: 845px; z-index: 2; text-align: right; color: #fff; font-size: 15px; line-height: 18px; }
  .contact-lines { right: 46px; top: 890px; z-index: 2; text-align: right; color: #fff; font-size: 13px; line-height: 14px; letter-spacing: 1.2px; }
  b { font-weight: 700; }
</style>
</head>
<body>
<main class="sheet">
  <div class="abs accent-bar"></div>
  <h1 class="abs title">Sample Merch Kit</h1>
  <p class="abs tagline">Quality Printing. On time, Every Time.</p>
  <div class="abs brand-mark"><div class="square"></div><div class="name">Copper Fern Prints</div></div>

  <h2 class="abs series">Series:<br>Summer/Fall 2025<br>Collection</h2>
  <div class="abs kit-label">Merch KIT CONTENTS</div>
  <ol class="abs kit-list">
    <li><span>1.</span>Custom Shop T-Shirt</li>
    <li><span>2.</span>Additional Sample Shirt</li>
    <li><span>3.</span>CFP Ink Pen</li>
  </ol>
  <div class="abs colors"><span class="label">COLORS</span>
    <i class="dot" style="background:var(--teal-deep)"></i><i class="dot" style="background:var(--blue-pale)"></i><i class="dot" style="background:var(--blue-deep)"></i><i class="dot" style="background:var(--gold)"></i>
  </div>
  <p class="abs sizes">Size: S,M,L,XL</p>
  <p class="abs warning">WARNING: These shirts may cause<br>increased shop morale,<br>envy from competitors, and a high<br>volume of customer demand.</p>

  <div class="abs side-tab"><span>CFP T-SHIRTS</span></div>
  <div class="model-label">MODEL</div>
  <div class="abs photo hero"><div class="fill" role="img" aria-label="Model t-shirt with front chest print" style="background:radial-gradient(circle at 50% 35%, var(--gold-soft) 0 14%, var(--teal-deep) 34%)"></div></div>

  <div class="abs photo thumb t1"><div class="fill" role="img" aria-label="Teal t-shirt with front print" style="background:radial-gradient(circle at 50% 32%, var(--gold-soft) 0 16%, var(--teal-deep) 36%)"></div></div>
  <div class="abs photo thumb t2"><div class="fill" role="img" aria-label="Blue t-shirt with front print" style="background:radial-gradient(circle at 50% 36%, var(--gold) 0 18%, var(--blue) 38%)"></div></div>
  <div class="abs photo thumb t3"><div class="fill" role="img" aria-label="Dark hoodie with chest print and sleeve lettering" style="background:radial-gradient(circle at 45% 38%, var(--teal-soft) 0 14%, var(--charcoal) 34%)"></div></div>

  <div class="abs footer"></div>
  <div class="abs footer-name">Copper Fern<br>Prints</div>
  <p class="abs invite">We'd love to work with you!</p>
  <p class="abs contact">Contact <b>Dana Whitlow</b> to start<br>your next shirt order today.</p>
  <p class="abs contact-lines"><b>Call</b> 555-014-2290 or<br><b>Email</b> dana@copperfernprints.com</p>
</main>
</body>
</html>
```